Geschäftspapiere für jungen Rechtsanwalt
Zielgruppe
'Voran' Rechtsanwaltskanzlei, die hauptsächlich im Verkehrsrecht tätig ist. Dabei sowohl für Otto-Normalbürger, als auch für Versicherungen.
Aufgabenstellung
Neben Postanschrift, Telefon, Faxnummer und E-Mail-Adresse sind Angaben zur Bankverbindung und Steuernummer erforderlich.
Bitte keine Klassiker, wie z.B. Paragraphenzeichen, Justizia, etc.

```html
<!DOCTYPE html>
<html lang="de">
<head>
<meta charset="utf-8">
<title>Geschäftspapiere Voran</title>
<link href="https://fonts.googleapis.com/css2?family=Arimo:wght@400;700&display=swap" rel="stylesheet">
<style>
  :root{
    --brand:#637277;
    --paper:#ffffff;
    --ground:#ffffff;
    --text:#6e7b80;
    --mark:#9aa3a6;
    --shadow:rgba(0,0,0,.45);
  }
  html,body{margin:0;padding:0;overflow:hidden;background:var(--ground);}
  .canvas{position:relative;width:1200px;height:840px;overflow:hidden;font-family:"Arimo",Arial,sans-serif;color:var(--text);}
  .abs{position:absolute;}
  .sheet{background:var(--paper);box-shadow:5px 6px 6px var(--shadow);}
  .band{position:absolute;background:var(--brand);}
  .brand-name{position:absolute;font-family:"Arimo",Arial,sans-serif;font-weight:400;color:var(--brand);letter-spacing:1px;line-height:1;white-space:nowrap;}
  .brand-name.on-band{color:var(--paper);}
  .crop{position:absolute;background:var(--mark);}
  .crop.h{height:1px;width:30px;}
  .crop.v{width:1px;height:30px;}
  .small{font-size:5px;line-height:7.7px;}
  .footer-text{position:absolute;color:var(--paper);font-size:6.8px;top:6px;white-space:nowrap;}

  /* letterhead */
  .letterhead{left:53px;top:53px;width:510px;height:721px;}
  .letterhead .sender-name{position:absolute;left:363px;top:41px;font-size:6.8px;font-weight:700;}
  .letterhead .sender-role{position:absolute;left:363px;top:50px;font-size:5px;}
  .letterhead .contact-block{position:absolute;left:363px;top:69px;}
  .letterhead .contact-block p{margin:0 0 7.7px;}
  .window-frame{position:absolute;left:46px;top:96px;}
  .return-line{position:absolute;left:83px;top:107px;font-size:4.6px;color:#b4bcbf;white-space:nowrap;}
  .return-line b{color:var(--brand);font-weight:700;}
  .fold{position:absolute;left:10px;width:10px;height:1px;background:var(--text);}

  /* business cards */
  .card{top:113px;width:252px;height:147px;}
  .card-front{left:649px;}
  .card-back{left:911px;}
  .card .holder{position:absolute;left:22px;top:65px;}
  .card .holder .name{font-size:6.8px;font-weight:700;}
  .card .holder .role{font-size:5px;margin-bottom:5px;}
  .card .holder p{margin:0 0 6px;}

  /* envelope */
  .envelope{left:626px;top:507px;width:535px;height:267px;}
  .flap{position:absolute;left:626px;top:405px;}
  .flap-text{position:absolute;left:800px;top:425px;width:190px;transform:rotate(180deg);text-align:center;}
  .flap-text .addr{font-size:7.4px;}
  .window{position:absolute;left:52px;top:108px;width:242px;height:107px;border:1px solid #c9cfd1;border-radius:10px;box-shadow:inset 2px 2px 5px rgba(0,0,0,.35);background:#fff;}
</style>
</head>
<body>
<div class="canvas">

  <!-- crop marks: letterhead -->
  <div class="crop v" style="left:53px;top:8px"></div>
  <div class="crop v" style="left:563px;top:8px"></div>
  <div class="crop h" style="left:8px;top:53px"></div>
  <div class="crop h" style="left:580px;top:53px"></div>
  <div class="crop h" style="left:8px;top:774px"></div>
  <div class="crop h" style="left:580px;top:774px"></div>
  <div class="crop v" style="left:53px;top:790px"></div>
  <div class="crop v" style="left:563px;top:790px"></div>
  <!-- crop marks: envelope -->
  <div class="crop h" style="left:626px;top:405px"></div>
  <div class="crop h" style="left:1135px;top:405px"></div>
  <div class="crop h" style="left:1168px;top:774px"></div>
  <div class="crop v" style="left:626px;top:785px"></div>
  <div class="crop v" style="left:1161px;top:785px"></div>

  <!-- letterhead -->
  <section class="sheet abs letterhead">
    <div class="band" style="left:-2px;top:32px;width:361px;height:30px"></div>
    <div class="band" style="left:462px;top:32px;width:48px;height:30px"></div>
    <div class="brand-name on-band" style="left:34px;top:39px;font-size:15px">VORAN</div>
    <div class="abs" style="left:55px;top:56px;font-size:4.8px;color:#fff;white-space:nowrap">Fernhagel Rechtsanwaltskanzlei</div>

    <div class="sender-name">Lukas Fernhagel, LL.M.</div>
    <div class="sender-role">Rechtsanwalt</div>
    <div class="contact-block small">
      <p><b>Kontakt</b><br>Tel.:&nbsp; 07351 5520180<br>Fax.:&nbsp; 07351 5520181</p>
      <p>Lindenweg 14<br>88410 Mühlbach</p>
      <p>Bankverbindung:<br>Kreissparkasse Talgau<br>IBAN: DE 12 6400 0000 0011 2233 44<br>BIC: TALGDE61XXX</p>
      <p>Steuernummer: 51220/48831<br>USt-IdNr.: DE294117360</p>
    </div>

    <svg class="window-frame" width="214" height="104" viewBox="0 0 214 104" aria-hidden="true">
      <g fill="none" stroke="#8a9498" stroke-width="0.8">
        <path d="M1 18 V10 A9 9 0 0 1 10 1 H18"/>
        <path d="M196 1 H204 A9 9 0 0 1 213 10 V18"/>
        <path d="M1 86 V94 A9 9 0 0 0 10 103 H18"/>
        <path d="M196 103 H204 A9 9 0 0 0 213 94 V86"/>
      </g>
    </svg>
    <div class="return-line"><b>VORAN</b> &bull; Lindenweg 14 &nbsp;&bull;&nbsp; 88410 Mühlbach</div>

    <div class="fold" style="top:248px"></div>
    <div class="fold" style="top:491px"></div>

    <div class="band" style="left:0;top:702px;width:510px;height:19px">
      <div class="footer-text" style="left:209px">E-Mail: info@verkehrsrecht-talheim.de</div>
      <svg class="abs" style="left:338px;top:0" width="28" height="19" aria-hidden="true">
        <path d="M2 19 L16 0 M10 19 L24 0" stroke="#fff" stroke-width="1"/>
      </svg>
      <div class="footer-text" style="left:377px">Web: www.verkehrsrecht-talheim.de</div>
    </div>
  </section>

  <!-- business card front -->
  <section class="sheet abs card card-front">
    <div class="band" style="left:0;top:54px;width:15px;height:30px"></div>
    <div class="band" style="left:124px;top:54px;width:128px;height:30px"></div>
    <div class="brand-name on-band" style="left:142px;top:62px;font-size:15px">VORAN</div>
    <div class="holder small">
      <div class="name">Lukas Fernhagel, LL.M.</div>
      <div class="role">Rechtsanwalt</div>
      <p><b>Kontakt</b><br>Tel.:&nbsp; 07351 5520180<br>Fax.:&nbsp; 07351 5520181<br>E-Mail: info@verkehrsrecht-talheim.de<br>Web: www.verkehrsrecht-talheim.de</p>
      <p>Lindenweg 14<br>88410 Mühlbach</p>
    </div>
  </section>

  <!-- business card back -->
  <section class="sheet abs card card-back">
    <div class="band" style="left:0;top:54px;width:20px;height:30px"></div>
    <div class="band" style="left:101px;top:54px;width:151px;height:30px"></div>
    <div class="brand-name" style="left:28px;top:62px;font-size:14px">VORAN</div>
  </section>

  <!-- envelope flap -->
  <svg class="flap" width="535" height="103" viewBox="0 0 535 103" aria-hidden="true">
    <path d="M38 1 H478 Q490 1 496 14 L535 103 H0 Z" fill="#fff" stroke="#e6e9ea" stroke-width="1"/>
    <path d="M0 102 H535" stroke="#d7dcdd" stroke-dasharray="5 4"/>
  </svg>
  <div class="flap-text">
    <div class="brand-name" style="position:static;font-size:15px;margin-bottom:8px">VORAN</div>
    <div class="addr">Lindenweg 14 &nbsp;&bull;&nbsp; 88410 Mühlbach</div>
  </div>

  <!-- envelope body -->
  <section class="sheet abs envelope">
    <div class="band" style="left:0;top:34px;width:48px;height:30px"></div>
    <div class="band" style="left:171px;top:34px;width:362px;height:30px"></div>
    <div class="brand-name" style="left:60px;top:40px;font-size:20px">VORAN</div>
    <div class="window"></div>
    <div class="band" style="left:0;top:248px;width:535px;height:19px">
      <div class="footer-text" style="left:234px">E-Mail: info@verkehrsrecht-talheim.de</div>
      <svg class="abs" style="left:363px;top:0" width="28" height="19" aria-hidden="true">
        <path d="M2 19 L16 0 M10 19 L24 0" stroke="#fff" stroke-width="1"/>
      </svg>
      <div class="footer-text" style="left:402px">Web: www.verkehrsrecht-talheim.de</div>
    </div>
  </section>

</div>
</body>
</html>
```